Business Card Design for Brightkeel

The company provides engineering tender consulting services and personnel resources. The target market is large engineering construction and services companies. The business is based in Australia.

```html
<!DOCTYPE html>
<html lang="en">
<head>
<meta charset="utf-8">
<title>Brightkeel Business Card</title>
<link href="https://fonts.googleapis.com/css2?family=Source+Sans+3:wght@400;600&display=swap" rel="stylesheet">
<style>
  :root {
    --backdrop: #cccccc;
    --card: #ffffff;
    --accent: #fdb550;
    --ink: #231f20;
    --on-accent: #ffffff;
  }
  * { margin: 0; padding: 0; box-sizing: border-box; }
  html, body {
    width: 1200px;
    height: 1000px;
    overflow: hidden;
    background: var(--backdrop);
    font-family: "Source Sans 3", "Myriad Pro", Arial, sans-serif;
    color: var(--ink);
  }
  .canvas { position: relative; width: 1200px; height: 1000px; }
  .card {
    position: absolute;
    top: 151px;
    width: 423px;
    height: 697px;
    background: var(--card);
  }
  .card--front { left: 117px; }
  .card--back { left: 659px; }
  .card__edge {
    position: absolute;
    left: 0;
    width: 100%;
    height: 13px;
    background: var(--accent);
  }
  .card__edge--top { top: 0; }
  .card__edge--bottom { bottom: 0; }
  .brand__dot {
    position: absolute;
    left: 13px;
    top: 51px;
    width: 96px;
    height: 96px;
  }
  .brand__band {
    position: absolute;
    left: 123px;
    top: 63px;
    right: 0;
    height: 63px;
    background: var(--accent);
    display: flex;
    align-items: center;
    padding-left: 42px;
  }
  .brand__name {
    color: var(--on-accent);
    font-weight: 600;
    font-size: 38px;
    letter-spacing: 1.5px;
    line-height: 1;
  }
  .brand__slogan {
    position: absolute;
    right: 18px;
    top: 136px;
    font-size: 12px;
    letter-spacing: 0.6px;
    text-transform: uppercase;
  }
  .holder {
    position: absolute;
    right: 84px;
    top: 328px;
    text-align: right;
  }
  .holder__name { font-size: 30px; font-weight: 400; line-height: 1.2; }
  .holder__position { font-size: 15px; margin-top: 6px; }
  .contact {
    position: absolute;
    left: 16px;
    top: 577px;
    list-style: none;
    font-size: 15px;
    line-height: 20px;
  }
  .services {
    position: absolute;
    left: 59px;
    top: 212px;
    list-style: none;
    font-size: 15px;
    line-height: 40px;
  }
</style>
</head>
<body>
<main class="canvas">
  <section class="card card--front" aria-label="Business card front">
    <div class="card__edge card__edge--top"></div>
    <svg class="brand__dot" viewBox="0 0 96 96" aria-hidden="true"><circle cx="48" cy="48" r="48" fill="var(--accent)"/></svg>
    <div class="brand__band"><span class="brand__name">Brightkeel</span></div>
    <p class="brand__slogan">Company Slogan</p>
    <div class="holder">
      <h1 class="holder__name">Tarrant Designs</h1>
      <p class="holder__position">Position</p>
    </div>
    <ul class="contact">
      <li>Mobile : 9999 999 999</li>
      <li>Telephone : 99 9999 9999</li>
      <li>E-mail : nnnn@nn.com.au</li>
      <li>PO BOX 99 Nnnnnnn, Nnn, 9999</li>
      <li>ABN9999999999999</li>
    </ul>
    <div class="card__edge card__edge--bottom"></div>
  </section>

  <section class="card card--back" aria-label="Business card back">
    <div class="card__edge card__edge--top"></div>
    <svg class="brand__dot" viewBox="0 0 96 96" aria-hidden="true"><circle cx="48" cy="48" r="48" fill="var(--accent)"/></svg>
    <div class="brand__band"><span class="brand__name">Brightkeel</span></div>
    <ul class="services">
      <li>Tender Strategy</li>
      <li>Bid Management</li>
      <li>Proposal Writing</li>
      <li>Cost Estimating</li>
      <li>Risk Assessment</li>
      <li>Compliance Review</li>
      <li>Contract Advice</li>
      <li>Project Staffing</li>
      <li>Technical Personnel</li>
      <li>Site Resourcing</li>
    </ul>
    <div class="card__edge card__edge--bottom"></div>
  </section>
</main>
</body>
</html>
```